Selvin: A Friday night in the Prophetic Flyer

We are holding 2 Friday night events, one on 10/25/19 and the other on 11/29/19.
The time frame is 6:30pm-9:00pm. These services will be a time of prayer/healing for the sick and will be prophetic as well. (There will be prophets prophesying over people)

The event is called: Selvin: A Friday night in the Prophetic
The flyer should also include the phrase/excerpt: "And they prophesied also".

Keywords/Phrases: Prophetic, Healing, Climbing in the Spirit, Higher level of Anointing...

Target Market(s)

those looking for healing, seeking a word from God

Colors

Designer to choose colors to be used in the design.

Requirements
Must have
• The event is called: Selvin: A Friday night in the Prophetic
• The flyer should also include the phrase/excerpt: "And they prophesied also".
• It must include the Tovik logo attached, either is fine, we have attached two different versions.
• It must have the dates, location, time
• Dates: October 25, 2019 and November 29, 2019
• Location: Hollard Community Center
• (Downtown Portland) 482 Wendle Street
• Portland, ME 04102
• Time: 6:30pm-9:00pm
• Contact Info: Tel. 207-555-3841
• email: contact@brimfield-hall.org
• web: www.tovik.org
Nice to have
• creativity in color scheme, the meaning of the word Selvin conveyed in a classy artistic way/design.
Should not have
• Crosses, pictures of churches

```html
<!DOCTYPE html>
<html lang="en">
<head>
<meta charset="utf-8">
<title>Selvin: A Friday Night in the Prophetic</title>
<link href="https://fonts.googleapis.com/css2?family=Marcellus+SC&family=Roboto+Condensed:wght@400;700&display=swap" rel="stylesheet">
<style>
  :root {
    --ink: #2b1712;
    --orange: #f39a26;
    --bronze: #8a5424;
    --frame: rgba(255, 244, 225, 0.75);
    --white: #ffffff;
    --cream: #fffdf8;
    --gold: #f6c45a;
    --amber: #e08a2c;
    --maroon: #3a1414;
  }
  html, body {
    margin: 0;
    padding: 0;
    overflow: hidden;
    background: var(--cream);
  }
  .flyer {
    position: relative;
    width: 927px;
    height: 1200px;
    overflow: hidden;
    font-family: "Marcellus SC", serif;
    color: var(--ink);
    text-align: center;
  }
  .backdrop {
    position: absolute;
    inset: 0;
    background:
      radial-gradient(ellipse 520px 360px at 210px 430px, rgba(255,255,235,0.95), rgba(255,240,190,0) 70%),
      linear-gradient(180deg,
        #ffffff 0px,
        #fffdf6 300px,
        #fbe9b8 390px,
        var(--gold) 520px,
        #eeae4c 640px,
        var(--amber) 760px,
        #b4582a 860px,
        #6e2a1e 950px,
        var(--maroon) 1060px,
        #2e1012 1200px);
  }
  .kicker {
    position: absolute;
    top: 52px;
    left: 0;
    right: 0;
    margin: 0;
    font-size: 31px;
    letter-spacing: 1px;
    font-weight: 400;
  }
  .event-name {
    position: absolute;
    top: 82px;
    left: 0;
    right: 0;
    margin: 0;
    font-size: 176px;
    line-height: 1;
    font-weight: 400;
    color: var(--orange);
    letter-spacing: 2px;
  }
  .scripture {
    position: absolute;
    top: 262px;
    left: 0;
    right: 0;
    margin: 0;
    font-size: 30px;
    letter-spacing: 1px;
  }
  .scripture .big { font-size: 56px; }
  .dates {
    position: absolute;
    top: 352px;
    left: 0;
    right: 0;
    margin: 0;
    color: var(--bronze);
    font-size: 28px;
    line-height: 48px;
    letter-spacing: 1px;
  }
  .dates .month { font-size: 40px; }
  .time {
    position: absolute;
    top: 466px;
    left: 0;
    right: 0;
    margin: 0;
    font-family: "Roboto Condensed", sans-serif;
    font-size: 36px;
    font-weight: 400;
    color: #1d0f0b;
  }
  .venue {
    position: absolute;
    top: 527px;
    left: 194px;
    width: 584px;
    height: 82px;
    margin: 0;
    padding: 0;
    box-sizing: border-box;
    border: 4px solid var(--frame);
    font-family: "Roboto Condensed", sans-serif;
    color: #1d0f0b;
  }
  .venue legend {
    padding: 0 14px;
    font-weight: 700;
    font-size: 24px;
    margin: 0 auto;
  }
  .venue p {
    margin: -4px 0 0;
    font-size: 23px;
    line-height: 31px;
  }
  .brand {
    position: absolute;
    top: 1005px;
    left: 0;
    right: 0;
    display: flex;
    justify-content: center;
    align-items: center;
    gap: 12px;
    font-size: 58px;
    color: var(--white);
    letter-spacing: 2px;
  }
  .brand .dot {
    width: 22px;
    height: 22px;
    border-radius: 50%;
    background: var(--orange);
  }
  .contact {
    position: absolute;
    top: 1116px;
    left: 0;
    width: 927px;
    height: 30px;
    font-family: "Roboto Condensed", sans-serif;
    font-size: 23px;
    color: var(--white);
  }
  .contact span { position: absolute; white-space: nowrap; }
  .contact .label { color: var(--orange); position: static; }
  .contact .tel { left: 84px; }
  .contact .email { left: 301px; }
  .contact .web { left: 648px; }
</style>
</head>
<body>
  <main class="flyer">
    <div class="backdrop" role="img" aria-label="Photograph of a person standing on a mountain peak with arms outstretched above misty hills in golden sunset light"></div>

    <p class="kicker">A Friday Night in the Prophetic</p>
    <h1 class="event-name">SELVIN</h1>
    <p class="scripture">and THEY <span class="big">PROPHESIED</span> also</p>

    <p class="dates">
      <span class="month">OCTOBER</span> 25, 2019<br>
      and <span class="month">NOVEMBER</span> 29, 2019
    </p>

    <p class="time">TIME: 6:30PM-9:00PM</p>

    <fieldset class="venue">
      <legend>Hollard Community Center</legend>
      <p>(Downtown Portland) 482 Wendle Street<br>Portland, ME 04102</p>
    </fieldset>

    <div class="brand"><span class="dot"></span><span>TOVIK</span></div>

    <div class="contact">
      <span class="tel"><span class="label">Tel.</span> 207-555-3841</span>
      <span class="email"><span class="label">email:</span> contact@brimfield-hall.org</span>
      <span class="web"><span class="label">web:</span> www.tovik.org</span>
    </div>
  </main>
</body>
</html>
```